Family cosmetic dental practice. Very friendly, relaxed environment. All aspects of modern dentistry with exceptional service.

Industry/Entity Type

Dental

Contact Information for Business Card

Mark T Halvorsen DMD, P.C. 814-555-0172
418 NORTH TILMANE
STATE COLLEGE, PA side2- www.fakebooklet.example/drmarkhalvorsen for news, free KVT Football tickets, promotions, etc.

Requirements
Must have
• face of male and female showing attractive smiles.

```html
<!DOCTYPE html>
<html lang="en">
<head>
<meta charset="utf-8">
<title>Halvorsen Dental – Business Card</title>
<link href="https://fonts.googleapis.com/css2?family=Arimo:wght@400;700&display=swap" rel="stylesheet">
<style>
  :root {
    --bg: #e4e4e4;
    --brand-blue: #1f7fce;
    --brand-blue-deep: #1a6fb8;
    --ink: #333333;
    --rule: #555555;
    --white: #ffffff;
    --photo-light: #f3f1ee;
    --photo-mid: #dcc9b8;
  }
  * { box-sizing: border-box; margin: 0; padding: 0; }
  html, body {
    width: 1200px; height: 777px; overflow: hidden;
    background: var(--bg);
    font-family: "Arimo", Arial, sans-serif;
  }
  .canvas {
    position: relative; width: 1200px; height: 777px;
    display: flex; align-items: center; justify-content: center; gap: 50px;
  }
  .card {
    width: 520px; height: 297px; position: relative; overflow: hidden;
    box-shadow: 0 2px 6px rgba(0,0,0,.15);
  }
  /* Back side */
  .card-back {
    background: linear-gradient(135deg, var(--brand-blue) 0%, var(--brand-blue-deep) 100%);
    color: var(--white);
    display: flex; flex-direction: column; align-items: center; justify-content: center;
    text-align: center;
  }
  .brand-mark {
    width: 40px; height: 40px; border: 3px solid currentColor; border-radius: 50%;
    margin-bottom: 10px;
  }
  .card-back .brand-name { font-size: 21px; font-weight: 700; letter-spacing: .5px; }
  .card-back .web { font-size: 10.5px; margin-top: 8px; opacity: .9; }
  .card-back .tagline { font-size: 10.5px; margin-top: 3px; opacity: .9; }
  /* Front side */
  .card-front { background: var(--white); }
  .photo {
    position: absolute; left: 0; top: 40px; width: 270px; height: 210px;
    background: radial-gradient(ellipse at 50% 45%, var(--photo-mid) 0%, var(--photo-light) 60%, var(--white) 85%);
  }
  .front-brand {
    position: absolute; left: 300px; top: 32px; width: 150px;
    display: flex; flex-direction: column; align-items: center;
    color: var(--brand-blue);
  }
  .front-brand .brand-mark { width: 22px; height: 22px; border-width: 2px; margin-bottom: 5px; }
  .front-brand .brand-name { font-size: 10px; font-weight: 700; letter-spacing: .3px; }
  .details { position: absolute; left: 300px; top: 110px; width: 190px; }
  .name { color: var(--brand-blue); font-size: 13px; }
  .title { color: var(--ink); font-size: 10px; margin-top: 2px; }
  .rule { height: 1px; background: var(--rule); margin: 9px 0; }
  .address { color: var(--ink); font-size: 10px; line-height: 1.5; }
  .phone { font-size: 10px; color: var(--ink); }
  .phone .label { color: var(--brand-blue); }
</style>
</head>
<body>
<main class="canvas">
  <section class="card card-back">
    <span class="brand-mark"></span>
    <div class="brand-name">HALVORSEN DENTAL</div>
    <p class="web">www.fakebooklet.example/drmarkhalvorsen</p>
    <p class="tagline">for news, free KVT Football tickets, promotions, etc.</p>
  </section>

  <section class="card card-front">
    <div class="photo" role="img" aria-label="Photo of a smiling older man and young woman, cheek to cheek, fading into white"></div>
    <div class="front-brand">
      <span class="brand-mark"></span>
      <div class="brand-name">HALVORSEN DENTAL</div>
    </div>
    <div class="details">
      <p class="name">Mark T Halvorsen</p>
      <p class="title">DMD, P.C.</p>
      <div class="rule"></div>
      <p class="address">418 NORTH TILMANE<br>STATE COLLEGE, PA</p>
      <div class="rule"></div>
      <p class="phone"><span class="label">Phone:</span> 814-555-0172</p>
    </div>
  </section>
</main>
</body>
</html>
```